Disability and mental health support work company requires business card

Specialising
Bellwind Disability is a new HVTA service aimed toward HVTA participants with a history of criminal justice, psychosocial/mental health, intellectual, and cognitive disabilities.

Our focus
Focusing on providing core HVTA supports for community participation, daily activities and supported independent living.

Authentic
Likeminded people wanting to make a difference in participant's lives.

Our aim to provide holistic and empowering supports targeted towards creating independence and guidance for all participants and families.
Over 35 years of experience working with people that have psychosocial, intellectual, and cognitive disabilities.

Industry/Entity Type

disability and mental health

Contact Information for Business Card

logo - business name

Colors
0054AA
0677BA
7BADD7
CADEEF
E8F1F8
FFF300
FFF600
FEFA6F
FFFEC7
FFFEE8

Requirements
Must have
• want double sided business cards(wont let me change it)
Should not have
• any disability related pictures

```html
<!DOCTYPE html>
<html lang="en">
<head>
<meta charset="utf-8">
<title>Bellwind Disability – Business Card</title>
<link rel="stylesheet" href="https://fonts.googleapis.com/css2?family=Poppins:wght@300;400;500;600;800&display=swap">
<style>
  :root {
    --navy: #153a63;
    --sky: #7badd7;
    --white: #ffffff;
    --ink: #111822;
    --backdrop: #eef1f5;
  }
  * { margin: 0; padding: 0; box-sizing: border-box; }
  html, body { width: 1200px; height: 900px; overflow: hidden; }
  body {
    background: var(--backdrop);
    font-family: "Poppins", sans-serif;
    position: relative;
  }
  .card {
    position: absolute;
    left: 300px;
    width: 600px;
    height: 343px;
    box-shadow: 0 8px 24px rgba(20, 40, 70, 0.18);
    overflow: hidden;
  }
  .card--back { top: 60px; background: var(--navy); }
  .card--front { top: 477px; background: var(--white); }
  .card__art { position: absolute; inset: 0; width: 100%; height: 100%; }
  .brand-name {
    font-family: "Poppins", sans-serif;
    font-weight: 600;
    fill: var(--sky);
  }
  .person { position: absolute; left: 40px; top: 40px; }
  .person__name {
    font-weight: 800;
    font-size: 26px;
    color: var(--navy);
    letter-spacing: 0.2px;
    line-height: 1.05;
  }
  .person__role {
    font-weight: 400;
    font-size: 17px;
    color: var(--sky);
    line-height: 1.1;
  }
  .contact { position: absolute; left: 40px; top: 126px; list-style: none; }
  .contact__item {
    display: flex;
    align-items: center;
    gap: 10px;
    font-size: 15px;
    color: var(--ink);
    line-height: 22px;
  }
  .contact__icon { width: 16px; height: 16px; flex: none; }
  .address { position: absolute; left: 66px; top: 210px; font-size: 15px; color: var(--ink); line-height: 21px; }
  .website {
    position: absolute;
    right: 36px;
    bottom: 46px;
    font-size: 14px;
    color: var(--white);
    letter-spacing: 0.3px;
  }
</style>
</head>
<body>

<section class="card card--back" aria-label="Card back">
  <svg class="card__art" viewBox="0 0 600 343">
    <circle cx="300" cy="171" r="100" fill="none" stroke="var(--sky)" stroke-width="3"/>
    <text class="brand-name" x="300" y="166" font-size="22" text-anchor="middle">Bellwind</text>
    <text class="brand-name" x="300" y="193" font-size="22" text-anchor="middle">Disability</text>
  </svg>
</section>

<section class="card card--front" aria-label="Card front">
  <svg class="card__art" viewBox="0 0 600 343" preserveAspectRatio="none">
    <path d="M0,286 C190,292 310,252 430,176 C330,256 200,300 0,304 Z" fill="var(--sky)"/>
    <path d="M0,304 C200,300 330,262 440,192 C510,148 560,122 600,112 L600,343 L0,343 Z" fill="var(--navy)"/>
    <circle cx="478" cy="96" r="74" fill="var(--navy)" stroke="var(--sky)" stroke-width="3"/>
    <text class="brand-name" x="478" y="92" font-size="18" text-anchor="middle">Bellwind</text>
    <text class="brand-name" x="478" y="114" font-size="18" text-anchor="middle">Disability</text>
  </svg>

  <div class="person">
    <h1 class="person__name">MARCUS HALE</h1>
    <p class="person__role">Managing Director</p>
  </div>

  <ul class="contact">
    <li class="contact__item">
      <svg class="contact__icon" viewBox="0 0 16 16"><path d="M3 1.5l2.6 0 1.2 3.2-1.7 1.1c.8 1.8 2.3 3.3 4.1 4.1l1.1-1.7 3.2 1.2v2.6c0 .8-.7 1.5-1.5 1.5C6.5 13.5 1.5 8.5 1.5 3c0-.8.7-1.5 1.5-1.5z" fill="var(--navy)"/></svg>
      055-210 387 614
    </li>
    <li class="contact__item">
      <svg class="contact__icon" viewBox="0 0 16 16"><rect x="3.5" y="1" width="9" height="14" rx="1.8" fill="none" stroke="var(--navy)" stroke-width="1.6"/><circle cx="8" cy="12.3" r="0.9" fill="var(--navy)"/></svg>
      055-210 387 615
    </li>
    <li class="contact__item">
      <svg class="contact__icon" viewBox="0 0 16 16"><rect x="1" y="3" width="14" height="10" fill="var(--navy)"/><path d="M1.5 3.5L8 9l6.5-5.5" fill="none" stroke="var(--white)" stroke-width="1.2"/></svg>
      hello@bellwind.com
    </li>
  </ul>

  <p class="address">17 Harrow Lane,<br>Eastvale, 30914</p>

  <p class="website">www.bellwinddisability.com</p>
</section>

</body>
</html>
```